Brantley Energy PowerPoint Design

Looking for a sleek PowerPoint design for our energy services company. We supply EV charging, Solar, Battery Storage and more.

Please make the background white with hints of gray and utilize the exact dark blue and light blue colors in the logo.

This design should be sharp with minimal round edges.

Colors

Designer to choose colors to be used in the design.

```html
<!DOCTYPE html>
<html lang="en">
<head>
<meta charset="utf-8">
<title>Brantley Energy – Presentation Deck</title>
<link href="https://fonts.googleapis.com/css2?family=Poppins:wght@400;500;600&display=swap" rel="stylesheet">
<style>
:root{
  --navy:#170f55;
  --blue:#36a9f5;
  --ink:#222233;
  --muted:#3c3c48;
  --gray-bg:#f0f0f2;
  --gray-line:#dcdce2;
  --bar-gray:#3a3a3a;
  --white:#ffffff;
}
*{margin:0;padding:0;box-sizing:border-box}
html,body{width:821px;height:1200px;overflow:hidden;background:var(--white)}
body{position:relative;font-family:'Poppins',sans-serif;color:var(--ink)}
.slide{position:absolute;width:382px;height:215px;background:var(--white);overflow:hidden;box-shadow:0 0 3px rgba(0,0,0,.18)}
.slide--gray{background:linear-gradient(135deg,#e9e9ec 0%,#f8f8f9 45%,#ececef 70%,#f6f6f7 100%)}
.abs{position:absolute}
.center{text-align:center}
.accent{color:var(--blue)}
.navy{color:var(--navy)}

/* brand mark */
.brand{position:absolute;display:flex;align-items:center;gap:3px;font-weight:600;color:var(--navy);letter-spacing:.2px;white-space:nowrap}
.brand__square{display:block;background:var(--navy)}
.brand--corner{right:9px;top:16px;font-size:5.2px}
.brand--corner .brand__square{width:7px;height:7px}

/* footer */
.footer{position:absolute;left:0;bottom:0;width:100%;height:11px;background:var(--navy);display:flex;align-items:center;font-size:3.6px;color:var(--white);font-weight:500}
.footer__copy{padding-left:12px;flex:1}
.footer__page{width:62px;height:100%;background:var(--blue);display:flex;align-items:center;justify-content:center}

/* headings */
.rule{position:absolute;height:1px;width:20px;background:var(--navy)}
.title{position:absolute;font-size:8.4px;font-weight:500;color:var(--navy);white-space:nowrap}
.body{font-size:3.8px;line-height:9.8px;color:var(--muted)}
.photo{position:absolute}

/* agenda */
.agenda-item{position:absolute;display:flex;align-items:center;gap:7px;font-size:4.4px;color:var(--muted)}
.agenda-item__dot{width:5px;height:5px;border-radius:50%;background:var(--navy);display:flex;align-items:center;justify-content:center}

/* features */
.feature__icon{position:absolute;width:16px;height:16px;display:flex;align-items:center;justify-content:center}
.feature__title{position:absolute;font-size:4.8px;font-weight:500}
.feature__text{position:absolute;font-size:3.7px;color:var(--muted)}

/* services */
.card{position:absolute;top:59px;width:91px;height:133px;border:1px solid #ececf0;background:var(--white)}
.card__title{position:absolute;top:9px;width:100%;text-align:center;font-size:5px;font-weight:500;color:var(--navy)}
.card__text{position:absolute;top:19px;left:4px;right:4px;text-align:center;font-size:3.7px;line-height:9.8px;color:var(--muted)}
.card__photo{position:absolute;left:3px;right:3px;top:66px;height:64px}

/* process */
.step__title{position:absolute;width:110px;text-align:center;font-size:5.6px;font-weight:500;color:var(--navy)}
.step__text{position:absolute;width:110px;text-align:center;font-size:3.9px;line-height:9.5px;color:var(--muted)}

/* Q&A */
.qa__num{position:absolute;width:13px;height:13px;border-radius:50%;background:var(--navy);color:var(--white);font-size:4.4px;display:flex;align-items:center;justify-content:center}
.qa__head{position:absolute;width:150px;font-size:4.7px;font-weight:600;line-height:11px;color:var(--navy)}
.qa__text{position:absolute;width:150px;font-size:3.8px;line-height:9.9px;color:var(--muted)}

/* graph */
.axis-label{position:absolute;font-size:4.8px;color:var(--ink);width:12px;text-align:right}
.group-label{position:absolute;font-size:3.8px;color:var(--ink);width:40px;text-align:center}
.note-box{position:absolute;left:250px;top:53px;width:111px;height:125px;background:var(--white);box-shadow:0 0 3px rgba(0,0,0,.2);padding:11px 5px;text-align:center;font-size:3.8px;line-height:9.9px;color:var(--muted)}

/* closing */
.contact{position:absolute;top:175px;left:0;width:100%;height:40px;background:var(--navy);color:var(--white)}
.contact__label{position:absolute;top:8px;font-size:4.8px;color:var(--blue);font-weight:500}
.contact__text{position:absolute;top:19px;font-size:4.1px;line-height:8.6px}
</style>
</head>
<body>

<!-- 1 Title -->
<section class="slide" style="left:21px;top:25px">
  <div class="abs" style="left:0;top:0;width:100%;height:1.5px;background:var(--navy)"></div>
  <div class="abs" style="left:0;bottom:0;width:100%;height:1.5px;background:var(--navy)"></div>
  <div class="abs" style="left:83px;top:47px;width:216px;height:121px;background:#f3f3f8"></div>
  <div class="brand" style="left:0;right:0;top:62px;justify-content:center;font-size:12px;gap:5px"><span class="brand__square" style="width:12px;height:12px"></span>BRANTLEY ENERGY</div>
  <div class="abs center" style="left:0;right:0;top:108px;font-size:6.8px;color:var(--ink)">ENERGY SERVICES COMPANY</div>
  <div class="abs center" style="left:0;right:0;top:124px;font-size:13.2px;font-weight:500;color:var(--navy)">LEADING THE CHARGE FOR A</div>
  <div class="abs center accent" style="left:0;right:0;top:145px;font-size:11.2px;font-weight:500">GREENER TOMORROW</div>
  <div class="abs" style="left:159px;top:171px;width:65px;height:13px;background:var(--navy);color:var(--white);font-size:4.8px;font-weight:500;display:flex;align-items:center;justify-content:center">11TH DECEMBER 2024</div>
</section>

<!-- 2 Cover photo -->
<section class="slide" style="left:419px;top:25px">
  <div class="photo" role="img" aria-label="Couple with coffee cups beside an electric car charging at a station among green trees" style="left:0;top:0;width:382px;height:164px;background:linear-gradient(120deg,#6d8c54 0%,#3c5130 30%,#c9cdd0 55%,#5f7a45 80%,#8aa36b 100%)"></div>
  <div class="abs" style="left:258px;top:156px;width:63px;height:12px;background:var(--navy);color:var(--white);font-size:4.6px;font-weight:500;display:flex;align-items:center;justify-content:center">11TH DECEMBER 2024</div>
  <div class="brand" style="left:19px;top:184px;font-size:6.4px"><span class="brand__square" style="width:9px;height:9px"></span>BRANTLEY ENERGY</div>
  <div class="abs" style="left:188px;top:175px;font-size:11.3px;font-weight:500;color:var(--navy)">LEADING THE CHARGE FOR A</div>
  <div class="abs accent" style="left:188px;top:193px;font-size:9.8px;font-weight:500">GREENER TOMORROW</div>
</section>

<!-- 3 Agenda -->
<section class="slide slide--gray" style="left:21px;top:264px">
  <div class="rule" style="left:17px;top:28px"></div>
  <div class="title" style="left:17px;top:33px">BRANTLEY <span class="accent">AGENDA</span></div>
  <p class="abs body" style="left:17px;top:53px;width:200px">Lorem ipsum dolor sit amet, consectetur adipiscing elit, sed do eiusmod tempor incididunt ut labore et dolore magna aliqua. Ut enim ad minim veniam, quis nostrud exercitation ullamco laboris nisi ut aliquip ex ea commodo consequat. Duis aute irure dolor in reprehenderit in voluptate velit esse cillum dolore eu fugiat nulla pariatur.</p>
  <div class="agenda-item" style="left:20px;top:104px"><span class="agenda-item__dot"><svg width="3" height="3" viewBox="0 0 3 3"><path d="M0.4 1.5H2.5M1.7 0.7L2.5 1.5L1.7 2.3" stroke="#fff" stroke-width=".5" fill="none"/></svg></span>TITLE SLIDE</div>
  <div class="agenda-item" style="left:20px;top:125px"><span class="agenda-item__dot"><svg width="3" height="3" viewBox="0 0 3 3"><path d="M0.4 1.5H2.5M1.7 0.7L2.5 1.5L1.7 2.3" stroke="#fff" stroke-width=".5" fill="none"/></svg></span>BRANTLEY AGENDA</div>
  <div class="agenda-item" style="left:20px;top:145px"><span class="agenda-item__dot"><svg width="3" height="3" viewBox="0 0 3 3"><path d="M0.4 1.5H2.5M1.7 0.7L2.5 1.5L1.7 2.3" stroke="#fff" stroke-width=".5" fill="none"/></svg></span>WHY CHOOSE US?</div>
  <div class="agenda-item" style="left:20px;top:166px"><span class="agenda-item__dot"><svg width="3" height="3" viewBox="0 0 3 3"><path d="M0.4 1.5H2.5M1.7 0.7L2.5 1.5L1.7 2.3" stroke="#fff" stroke-width=".5" fill="none"/></svg></span>OUR SERVICES</div>
  <div class="agenda-item" style="left:108px;top:104px"><span class="agenda-item__dot"><svg width="3" height="3" viewBox="0 0 3 3"><path d="M0.4 1.5H2.5M1.7 0.7L2.5 1.5L1.7 2.3" stroke="#fff" stroke-width=".5" fill="none"/></svg></span>OUR PROCESS</div>
  <div class="agenda-item" style="left:108px;top:125px"><span class="agenda-item__dot"><svg width="3" height="3" viewBox="0 0 3 3"><path d="M0.4 1.5H2.5M1.7 0.7L2.5 1.5L1.7 2.3" stroke="#fff" stroke-width=".5" fill="none"/></svg></span>QUESTIONS &amp; ANSWERS</div>
  <div class="agenda-item" style="left:108px;top:145px"><span class="agenda-item__dot"><svg width="3" height="3" viewBox="0 0 3 3"><path d="M0.4 1.5H2.5M1.7 0.7L2.5 1.5L1.7 2.3" stroke="#fff" stroke-width=".5" fill="none"/></svg></span>OUR GRAPH</div>
  <div class="agenda-item" style="left:108px;top:166px"><span class="agenda-item__dot"><svg width="3" height="3" viewBox="0 0 3 3"><path d="M0.4 1.5H2.5M1.7 0.7L2.5 1.5L1.7 2.3" stroke="#fff" stroke-width=".5" fill="none"/></svg></span>THANK YOU</div>
  <div class="photo" role="img" aria-label="Light bulb containing a landscape with solar panels and wind turbines" style="left:222px;top:68px;width:132px;height:82px;border-radius:40px 20px 20px 40px;background:radial-gradient(circle at 30% 50%,#4f8fd8 0%,#6fae4a 55%,rgba(60,60,60,.85) 85%,rgba(240,240,242,0) 100%)"></div>
  <div class="brand brand--corner"><span class="brand__square"></span>BRANTLEY ENERGY</div>
  <footer class="footer"><span class="footer__copy">©2024 COPYRIGHTS <span class="accent">BRANTLEY ENERGY</span> &nbsp;| &nbsp;ALL RIGHTS RESERVED</span><span class="footer__page">PAGE 02</span></footer>
</section>

<!-- 4 Why choose us -->
<section class="slide" style="left:419px;top:264px">
  <div class="rule" style="left:181px;top:18px"></div>
  <div class="title center" style="left:0;right:0;top:23px">WHY CHOOSE <span class="accent">US?</span></div>
  <p class="abs body center" style="left:40px;width:302px;top:42px">Lorem ipsum dolor sit amet, consectetur adipiscing elit, sed do eiusmod tempor incididunt ut labore et dolore magna aliqua. Ut enim ad minim veniam, quis nostrud exercitation ullamco laboris nisi ut aliquip ex ea commodo consequat.</p>
  <div class="photo" role="img" aria-label="Battery storage facility at sunset surrounded by solar panels and hills" style="left:17px;top:74px;width:150px;height:116px;background:linear-gradient(180deg,#e7a15a 0%,#c98d5d 35%,#7b6f6e 60%,#4f5a6e 100%)"></div>
  <div class="abs body center" style="left:17px;top:162px;width:150px;height:28px;background:rgba(23,15,85,.88);color:var(--white);padding-top:4px">Lorem ipsum dolor sit amet, consectetur adipiscing elit, sed do eiusmod tempor incididunt ut</div>

  <div class="feature__icon" style="left:185px;top:74px;background:var(--navy)"><svg width="9" height="9" viewBox="0 0 10 10" fill="none" stroke="#fff" stroke-width=".7"><circle cx="5" cy="5" r="4"/><circle cx="5" cy="4" r="1.3"/><path d="M2.8 8C3.3 6.6 6.7 6.6 7.2 8"/></svg></div>
  <div class="feature__title navy" style="left:211px;top:74px">EXPERTISE</div>
  <div class="feature__text" style="left:211px;top:85px">Decades of experience in energy solutions.</div>

  <div class="feature__icon" style="left:185px;top:107px;background:var(--blue)"><svg width="9" height="9" viewBox="0 0 10 10" fill="none" stroke="#fff" stroke-width=".7"><path d="M5 1.5a2.8 2.8 0 0 1 1.6 5.1V8H3.4V6.6A2.8 2.8 0 0 1 5 1.5z"/><path d="M3.6 9h2.8"/></svg></div>
  <div class="feature__title accent" style="left:211px;top:107px">TAILORED SOLUTIONS</div>
  <div class="feature__text" style="left:211px;top:118px">Customized for your specific needs.</div>

  <div class="feature__icon" style="left:185px;top:140px;background:var(--navy)"><svg width="9" height="9" viewBox="0 0 10 10" fill="none" stroke="#fff" stroke-width=".7"><rect x="1.5" y="3" width="7" height="6"/><path d="M1 3L5 1l4 2M3.5 5v3M5 5v3M6.5 5v3"/></svg></div>
  <div class="feature__title navy" style="left:211px;top:140px">SUSTAINABILITY</div>
  <div class="feature__text" style="left:211px;top:151px">We are committed to helping our clients reduce their environmental impact.</div>

  <div class="feature__icon" style="left:185px;top:173px;background:var(--blue)"><svg width="9" height="9" viewBox="0 0 10 10" fill="none" stroke="#fff" stroke-width=".7"><circle cx="4" cy="4" r="2.5"/><circle cx="6.5" cy="6.5" r="2.5"/></svg></div>
  <div class="feature__title accent" style="left:211px;top:173px">CUSTOMER SATISFACTION</div>
  <div class="feature__text" style="left:211px;top:184px">Proven track record of client satisfaction and success.</div>

  <div class="brand brand--corner"><span class="brand__square"></span>BRANTLEY ENERGY</div>
  <footer class="footer"><span class="footer__copy">©2024 COPYRIGHTS <span class="accent">BRANTLEY ENERGY</span> &nbsp;| &nbsp;ALL RIGHTS RESERVED</span><span class="footer__page">PAGE 03</span></footer>
</section>

<!-- 5 Services -->
<section class="slide" style="left:21px;top:501px">
  <div class="rule" style="left:181px;top:16px"></div>
  <div class="title center" style="left:0;right:0;top:21px">OUR <span class="accent">SERVICES</span></div>
  <div class="abs center" style="left:0;right:0;top:39px;font-size:6.3px;color:var(--ink)">INNOVATING TOMORROW’S ENERGY SOLUTIONS</div>
  <article class="card" style="left:6px"><h3 class="card__title">EV CHARGING</h3><p class="card__text">Lorem ipsum dolor sit amet, consectetur adipiscing elit, sed do eiusmod tempor incididunt ut labore et dolore magna aliqua.</p><div class="card__photo" role="img" aria-label="Electric car plugged into a charging station on a city street" style="background:linear-gradient(135deg,#9aa2a8,#d8dcdf 50%,#6e7a70)"></div></article>
  <article class="card" style="left:100px"><h3 class="card__title">SOLAR POWER</h3><p class="card__text">Lorem ipsum dolor sit amet, consectetur adipiscing elit, sed do eiusmod tempor incididunt ut labore et dolore magna aliqua.</p><div class="card__photo" role="img" aria-label="Installers in safety vests fitting solar panels on a roof" style="background:linear-gradient(160deg,#8fb6de,#3b5f95 60%,#c7cc5a)"></div></article>
  <article class="card" style="left:194px"><h3 class="card__title">BATTERY STORAGE</h3><p class="card__text">Lorem ipsum dolor sit amet, consectetur adipiscing elit, sed do eiusmod tempor incididunt ut labore et dolore magna aliqua.</p><div class="card__photo" role="img" aria-label="Battery storage units among solar rows and wind turbines on green fields" style="background:linear-gradient(180deg,#a8cdef,#6e9bc5 45%,#6fa84a)"></div></article>
  <article class="card" style="left:288px"><h3 class="card__title">ENERGY MANAGEMENT</h3><p class="card__text">Lorem ipsum dolor sit amet, consectetur adipiscing elit, sed do eiusmod tempor incididunt ut labore et dolore magna aliqua.</p><div class="card__photo" role="img" aria-label="Hand holding a glowing light bulb surrounded by energy icons on green" style="background:radial-gradient(circle at 50% 45%,#d7e7a0,#5b8c3a 55%,#2b4a25)"></div></article>
  <div class="brand brand--corner"><span class="brand__square"></span>BRANTLEY ENERGY</div>
  <footer class="footer"><span class="footer__copy">©2024 COPYRIGHTS <span class="accent">BRANTLEY ENERGY</span> &nbsp;| &nbsp;ALL RIGHTS RESERVED</span><span class="footer__page">PAGE 04</span></footer>
</section>

<!-- 6 Process -->
<section class="slide slide--gray" style="left:419px;top:501px">
  <div class="rule" style="left:17px;top:18px"></div>
  <div class="title" style="left:17px;top:23px">OUR <span class="accent">PROCESS</span></div>
  <svg class="abs" style="left:0;top:0" width="382" height="215" viewBox="0 0 382 215">
    <polyline points="104,104 157,127 210,104 263,127 317,104" fill="none" stroke="#dedee3" stroke-width="14"/>
    <g fill="#dedee3">
      <circle cx="104" cy="104" r="22"/><circle cx="157" cy="127" r="22"/><circle cx="210" cy="104" r="22"/><circle cx="263" cy="127" r="22"/><circle cx="317" cy="104" r="22"/>
    </g>
    <g fill="#fff">
      <circle cx="104" cy="104" r="16"/><circle cx="157" cy="127" r="16"/><circle cx="210" cy="104" r="16"/><circle cx="263" cy="127" r="16"/><circle cx="317" cy="104" r="16"/>
    </g>
    <g fill="none" stroke="#170f55" stroke-width=".8">
      <rect x="98" y="98" width="10" height="8"/><path d="M100 104l2-2 2 1 3-3"/><circle cx="108" cy="107" r="2.3" stroke="#36a9f5"/>
      <circle cx="157" cy="124" r="2"/><circle cx="151" cy="126" r="1.6"/><circle cx="163" cy="126" r="1.6"/><path d="M150 132h14v-2h-14z"/>
      <circle cx="210" cy="104" r="6"/><circle cx="210" cy="104" r="2.2" stroke="#36a9f5"/>
      <circle cx="262" cy="125" r="3"/><path d="M257 133c1-3 9-3 10 0"/><rect x="264" y="119" width="6" height="4" stroke="#36a9f5"/>
      <path d="M312 98l5-2 5 2v6l-5 2-5-2z"/><path d="M311 110h12" stroke="#36a9f5"/>
    </g>
    <g stroke="#170f55" stroke-width="1" stroke-dasharray="1 2.2">
      <line x1="157" y1="92" x2="157" y2="101"/><line x1="263" y1="92" x2="263" y2="101"/>
      <line x1="104" y1="130" x2="104" y2="141"/><line x1="210" y1="130" x2="210" y2="141"/><line x1="317" y1="130" x2="317" y2="141"/>
    </g>
  </svg>
  <div class="step__title" style="left:107px;top:34px">CONSULTATION</div>
  <p class="step__text" style="left:107px;top:44px">Lorem ipsum dolor sit amettur adipiscing elit, sed do eiusmod tempor incididunt ut labore et dolore magna aliqua.</p>
  <div class="step__title" style="left:208px;top:38px">SUPPORT</div>
  <p class="step__text" style="left:208px;top:48px;padding:0 12px">Lorem ipsum dolor sit amet, consectetur adipiscing elit, sed do eiusmod tempor</p>
  <div class="step__title" style="left:46px;top:144px">OUR IMPACT</div>
  <p class="step__text" style="left:46px;top:154px">Lorem ipsum dolor sit amet, consectetur adipiscing elit, sed do eiusmod tempor incididunt</p>
  <div class="step__title" style="left:157px;top:144px">INSTALLATION</div>
  <p class="step__text" style="left:157px;top:154px">Lorem ipsum dolor sit amet, consectetur adipiscing elit, sed do eiusmod tempor incididunt</p>
  <div class="step__title" style="left:262px;top:144px">DESIGN</div>
  <p class="step__text" style="left:262px;top:154px">Lorem ipsum dolor sit amet, adipiscing elit, sed do eiusmod tempor incididunt ut labore et dolore magna aliqua.</p>
  <div class="brand brand--corner"><span class="brand__square"></span>BRANTLEY ENERGY</div>
  <footer class="footer"><span class="footer__copy">©2024 COPYRIGHTS <span class="accent">BRANTLEY ENERGY</span> &nbsp;| &nbsp;ALL RIGHTS RESERVED</span><span class="footer__page">PAGE 05</span></footer>
</section>

<!-- 7 Q&A -->
<section class="slide" style="left:21px;top:737px">
  <div class="rule" style="left:181px;top:18px"></div>
  <div class="title center" style="left:0;right:0;top:23px">QUESTIONS &amp; <span class="accent">ANSWERS</span></div>
  <p class="abs body center" style="left:45px;width:292px;top:40px">Lorem ipsum dolor sit amet, consectetur adipiscing elit, sed do eiusmod tempor incididunt ut labore et dolore magna aliqua. Ut enim ad minim veniam, quis nostrud exercitation ullamco laboris nisi ut aliquip ex ea commodo consequat.</p>
  <div class="qa__num" style="left:12px;top:72px">01</div>
  <div class="qa__head" style="left:34px;top:67px">LOREM IPSUM DOLOR SIT AMET CONSECTETUR ADIPISCING ELIT ?</div>
  <p class="qa__text" style="left:34px;top:91px">Lorem ipsum dolor sit amet, consectetur adipiscing elit, sed do eiusmod tempor incididunt ut labore et dolore magna aliqua. Ut enim ad minim veniam.</p>
  <div class="qa__num" style="left:199px;top:72px">03</div>
  <div class="qa__head" style="left:221px;top:67px">LOREM IPSUM DOLOR SIT AMET CONSECTETUR ADIPISCING ELIT ?</div>
  <p class="qa__text" style="left:221px;top:91px">Lorem ipsum dolor sit amet, consectetur adipiscing elit, sed do eiusmod tempor incididunt ut labore et dolore magna aliqua. Ut enim ad minim veniam.</p>
  <div class="qa__num" style="left:12px;top:136px">02</div>
  <div class="qa__head" style="left:34px;top:131px">LOREM IPSUM DOLOR SIT AMET CONSECTETUR ADIPISCING ELIT ?</div>
  <p class="qa__text" style="left:34px;top:155px">Lorem ipsum dolor sit amet, consectetur adipiscing elit, sed do eiusmod tempor incididunt ut labore et dolore magna aliqua. Ut enim ad minim veniam.</p>
  <div class="qa__num" style="left:199px;top:136px">04</div>
  <div class="qa__head" style="left:221px;top:131px">LOREM IPSUM DOLOR SIT AMET CONSECTETUR ADIPISCING ELIT ?</div>
  <p class="qa__text" style="left:221px;top:155px">Lorem ipsum dolor sit amet, consectetur adipiscing elit, sed do eiusmod tempor incididunt ut labore et dolore magna aliqua. Ut enim ad minim veniam.</p>
  <div class="brand brand--corner"><span class="brand__square"></span>BRANTLEY ENERGY</div>
  <footer class="footer"><span class="footer__copy">©2024 COPYRIGHTS <span class="accent">BRANTLEY ENERGY</span> &nbsp;| &nbsp;ALL RIGHTS RESERVED</span><span class="footer__page">PAGE 06</span></footer>
</section>

<!-- 8 Graph -->
<section class="slide" style="left:419px;top:737px">
  <div class="rule" style="left:181px;top:18px"></div>
  <div class="title center" style="left:0;right:0;top:23px">OUR <span class="accent">GRAPH</span></div>
  <div class="axis-label" style="left:15px;top:58px">70</div>
  <div class="axis-label" style="left:15px;top:73px">60</div>
  <div class="axis-label" style="left:15px;top:88px">50</div>
  <div class="axis-label" style="left:15px;top:103px">40</div>
  <div class="axis-label" style="left:15px;top:118px">30</div>
  <div class="axis-label" style="left:15px;top:133px">20</div>
  <div class="axis-label" style="left:15px;top:147px">10</div>
  <div class="axis-label" style="left:15px;top:162px">0</div>
  <svg class="abs" style="left:0;top:0" width="240" height="180" viewBox="0 0 240 180">
    <g stroke="#e4e4e8" stroke-width=".5">
      <line x1="35" y1="61" x2="217" y2="61"/><line x1="35" y1="76" x2="217" y2="76"/><line x1="35" y1="91" x2="217" y2="91"/><line x1="35" y1="106" x2="217" y2="106"/><line x1="35" y1="121" x2="217" y2="121"/><line x1="35" y1="135" x2="217" y2="135"/><line x1="35" y1="150" x2="217" y2="150"/>
    </g>
    <line x1="35" y1="165" x2="217" y2="165" stroke="#bdbdc4" stroke-width=".6"/>
    <g fill="#170f55"><rect x="42" y="147.1" width="6.5" height="17.9"/><rect x="88" y="150.1" width="6.5" height="14.9"/><rect x="134" y="132.2" width="6.5" height="32.8"/><rect x="180" y="118.8" width="6.5" height="46.2"/></g>
    <g fill="#36a9f5"><rect x="52.5" y="159" width="6.5" height="6"/><rect x="98.5" y="156" width="6.5" height="9"/><rect x="144.5" y="118.8" width="6.5" height="46.2"/><rect x="190.5" y="81.6" width="6.5" height="83.4"/></g>
    <g fill="#3a3a3a"><rect x="63" y="109.9" width="6.5" height="55.1"/><rect x="109" y="159" width="6.5" height="6"/><rect x="155" y="97.9" width="6.5" height="67.1"/><rect x="201" y="100.9" width="6.5" height="64.1"/></g>
  </svg>
  <div class="group-label" style="left:36px;top:171px">LOREM IPSUM</div>
  <div class="group-label" style="left:82px;top:171px">LOREM IPSUM</div>
  <div class="group-label" style="left:128px;top:171px">LOREM IPSUM</div>
  <div class="group-label" style="left:174px;top:171px">LOREM IPSUM</div>
  <div class="note-box">Lorem ipsum dolor sit amet, consectetur adipiscing elit, sed do eiusmod tempor incididunt ut labore et dolore magna aliqua. Ut enim ad minim quis nostrud exercitation ullamco laboris nisi ut aliquip ex ea commodo consequat. Duis aute irure dolor in reprehenderit in voluptate velit esse cillum dolore eu fugiat nulla pariatur.<br>Lorem ipsum dolor sit amet, consectetur adipiscing elit, sed do eiusmod tempor incididunt ut labore et dolore magna aliqua.</div>
  <div class="brand brand--corner"><span class="brand__square"></span>BRANTLEY ENERGY</div>
  <footer class="footer"><span class="footer__copy">©2024 COPYRIGHTS <span class="accent">BRANTLEY ENERGY</span> &nbsp;| &nbsp;ALL RIGHTS RESERVED</span><span class="footer__page">PAGE 07</span></footer>
</section>

<!-- 9 Closing -->
<section class="slide" style="left:220px;top:968px">
  <div class="photo" role="img" aria-label="Aerial view of wind turbines over a forest and a solar farm under a blue sky" style="left:0;top:0;width:382px;height:175px;background:linear-gradient(180deg,#3f7fd1 0%,#7fb0e6 40%,#c9d6de 55%,#6d7a4c 68%,#3e4d2c 85%,#2a3a55 100%)"></div>
  <div class="brand" style="left:0;right:0;top:22px;justify-content:center;font-size:10px;color:var(--white);gap:5px"><span class="brand__square" style="width:10px;height:10px;background:var(--white)"></span>BRANTLEY ENERGY</div>
  <div class="contact">
    <svg class="abs" style="left:37px;top:8px" width="6" height="6" viewBox="0 0 6 6"><path d="M3 .5a1.8 1.8 0 0 1 1.8 1.8C4.8 3.6 3 5.5 3 5.5S1.2 3.6 1.2 2.3A1.8 1.8 0 0 1 3 .5z" fill="#fff"/><circle cx="3" cy="2.3" r=".6" fill="#170f55"/></svg>
    <div class="contact__label" style="left:48px">ADDRESS</div>
    <div class="contact__text" style="left:48px">45 SOLAR WAY, SUITE 10,<br>BRIGHTFIELD, STATE 54321.</div>
    <svg class="abs" style="left:179px;top:9px" width="6" height="5" viewBox="0 0 6 5"><rect x=".3" y=".5" width="5.4" height="4" fill="#fff"/><path d="M.3 .5L3 2.7 5.7 .5" stroke="#170f55" stroke-width=".5" fill="none"/></svg>
    <div class="contact__label" style="left:193px">MAIL US</div>
    <div class="contact__text" style="left:193px">INFO@BRANTLEYENERGY.COM</div>
    <svg class="abs" style="left:302px;top:8px" width="6" height="6" viewBox="0 0 6 6"><path d="M1.2.5l1 1.4-.6.8c.4.9 1 1.5 1.9 1.9l.8-.6 1.4 1-.6.9C3.2 5.7.4 2.9.3 1.1z" fill="#fff"/></svg>
    <div class="contact__label" style="left:314px">CALL US</div>
    <div class="contact__text" style="left:314px">555-010-2468</div>
  </div>
</section>

</body>
</html>
```